HIgh-end jewelry designer needs a business card design

I need a business card design for the ecclectic & rather expensive jewelry designs. My approach to my work is to combine very old jewelry offset with contemporary items. I enjoy the idea of legacy as well as repurposing finely crafted items that are not possible to create any longer. My desire is to celebrate the past in a contemporary & funky way. The name of my business is VELLORINE. I see my business card design as simple & yet enigmatic as possible. In the end... clean, simple & understated is the look I am after. Thank you for your consideration...

Target Market(s)

I will use this business card for the trade as well as customers

Industry/Entity Type

Business

Contact Information for Business Card

Marta Quorrin Owner/Designer 555-203-7718

Requirements
Must have
• Clean & simple sophisticated design using the word "Vellorinne" as the logo. I like the idea of a play on the word itself, perhaps even using different fonts (i.e.: a bold helvetica combined with a lovely script). I'm afraid to say more because I don't want to limit creative input. Gosh, sometimes it's ok to break the rules!
Nice to have
• In my mind, I have imagined this business card to be simple, using my company name "Vellorine" in a playful yet sophisticated manner. I believe that doing something beautifully simple can be a true challenge. I have imagined something with just black & white, however I am open to ideas... after all that's why I'm here!
Should not have
• As Mozart once said... "It has too many notes!" I know I'm being silly, but I don't want it to be complicated or overly ornate.

```html
<!DOCTYPE html>
<html lang="en">
<head>
<meta charset="utf-8">
<title>Vellorine — Business Card</title>
<link href="https://fonts.googleapis.com/css2?family=Cinzel:wght@500;600&display=swap" rel="stylesheet">
<style>
  :root {
    --page-bg: #f1f1f0;
    --card-black: #0e0f10;
    --card-ink: #151617;
    --photo-warm: #4a3a2c;
    --photo-silver: #5d5f61;
    --band-light: rgba(255, 255, 255, 0.13);
    --band-soft: rgba(255, 255, 255, 0.07);
    --gold: #b8925a;
    --silver-text: #8c8c8c;
    --mark-fill: #cfcfcf;
    --edge-text: #3a3b3d;
  }
  * { margin: 0; padding: 0; box-sizing: border-box; }
  html, body {
    width: 1200px;
    height: 800px;
    overflow: hidden;
    background: var(--page-bg);
  }
  .card {
    position: absolute;
    left: 75px;
    top: 100px;
    width: 1050px;
    height: 600px;
    background: var(--card-black);
    overflow: hidden;
    font-family: "Cinzel", serif;
  }
  .card__photo {
    position: absolute;
    left: 0;
    top: 0;
    width: 720px;
    height: 470px;
    background:
      radial-gradient(ellipse 38% 30% at 62% 30%, var(--photo-silver) 0%, rgba(93,95,97,0) 70%),
      radial-gradient(ellipse 55% 45% at 48% 55%, var(--photo-warm) 0%, rgba(74,58,44,0.35) 45%, rgba(14,15,16,0) 80%);
  }
  .card__band {
    position: absolute;
    right: 0;
  }
  .card__band--upper {
    left: 400px;
    top: 200px;
    height: 52px;
    background: var(--band-light);
  }
  .card__band--lower {
    left: 470px;
    top: 252px;
    height: 130px;
    background: var(--band-soft);
  }
  .brand {
    position: absolute;
    left: 420px;
    top: 212px;
    display: flex;
    align-items: center;
    gap: 34px;
  }
  .brand__mark {
    width: 96px;
    height: 96px;
    background: var(--mark-fill);
  }
  .brand__text {
    display: flex;
    flex-direction: column;
    gap: 10px;
    padding-top: 40px;
  }
  .brand__name {
    font-size: 68px;
    font-weight: 600;
    letter-spacing: 4px;
    color: var(--gold);
    line-height: 1;
  }
  .brand__role {
    font-size: 26px;
    font-weight: 500;
    letter-spacing: 13px;
    color: var(--silver-text);
    line-height: 1;
  }
  .card__edge-note {
    position: absolute;
    left: 18px;
    top: 320px;
    transform: rotate(-90deg);
    transform-origin: left top;
    font-size: 14px;
    letter-spacing: 2px;
    color: var(--edge-text);
  }
</style>
</head>
<body>
  <section class="card">
    <div class="card__photo" role="img" aria-label="Photograph of an antique gold and diamond-set ring on a dark background"></div>
    <div class="card__band card__band--upper"></div>
    <div class="card__band card__band--lower"></div>
    <div class="brand">
      <div class="brand__mark"></div>
      <div class="brand__text">
        <span class="brand__name">VELLORINE</span>
        <span class="brand__role">JEWELRY DESIGNER</span>
      </div>
    </div>
    <span class="card__edge-note">Fine Pieces</span>
  </section>
</body>
</html>
```